Article/Flyer - Reservation of Rights

We would like an article that we normally produce through illustrator in a pdf format to be placed in a Word format. We have provided a sample article/flyer of our normal distribution style. We would like the outcome to be in WORD format

```html
<!DOCTYPE html>
<html lang="en">
<head>
<meta charset="utf-8">
<title>Reservation of Rights – Flyer</title>
<link rel="stylesheet" href="https://fonts.googleapis.com/css2?family=Lato:wght@400;700&display=swap">
<style>
  :root {
    --stage: #e6e9ed;
    --paper: #ffffff;
    --ink: #3a3a3a;
    --accent: #e0584f;
    --brand: #5f5f5f;
    --rule: #c9c9c9;
    --band: #a9a9a9;
    --photo-light: #f3f4f6;
    --photo-mid: #c7ccd3;
    --photo-dark: #8f99a6;
  }
  * { margin: 0; padding: 0; box-sizing: border-box; }
  html, body { width: 1200px; height: 770px; overflow: hidden; }
  body { background: var(--stage); font-family: "Lato", sans-serif; color: var(--ink); }

  .flyer {
    position: absolute; left: 313px; top: 15px;
    width: 573px; height: 740px;
    background: var(--paper);
    box-shadow: 0 2px 8px rgba(0,0,0,.25);
    overflow: hidden;
  }
  .masthead { position: relative; height: 200px; }
  .masthead-photo {
    position: absolute; inset: 0;
    background: linear-gradient(100deg, var(--photo-light) 0%, var(--photo-light) 35%, var(--photo-mid) 60%, var(--photo-dark) 100%);
  }
  .brand { position: absolute; left: 50px; top: 24px; }
  .brand-name {
    font-family: "Lato", sans-serif; font-weight: 400;
    font-size: 26px; color: var(--brand); line-height: 1;
  }
  .brand-line {
    font-size: 9px; color: var(--brand); margin-top: 6px;
  }
  .divider { height: 9px; background: var(--rule); }

  .body { padding: 17px 32px 0 32px; font-size: 7.9px; line-height: 1.45; }
  .columns { display: flex; gap: 28px; }
  .col { flex: 1; }
  .body p { margin-bottom: 10px; }
  .body h2 {
    color: var(--accent); font-weight: 400; font-size: 11px;
    margin: 14px 0 12px;
  }
  .col h2:first-child { margin-top: 0; font-weight: 700; font-size: 9px; }
  .full h2 { margin: 6px 0 3px; }
  .full p { margin-bottom: 8px; }

  .footer-band { position: absolute; left: 0; right: 0; bottom: 0; height: 27px; background: var(--band); }
</style>
</head>
<body>
<article class="flyer">
  <header class="masthead">
    <div class="masthead-photo" role="img" aria-label="Office team reviewing documents at a desk beside city high-rise buildings and a rolled insurance certificate"></div>
    <div class="brand">
      <div class="brand-name">Marlow Partners</div>
      <div class="brand-line">Insurance guidance for design and consulting firms</div>
    </div>
  </header>
  <div class="divider"></div>

  <section class="body">
    <div class="columns">
      <div class="col">
        <p>Reporting a claim or potential claim to your professional liability insurance company will produce a fair amount of return correspondence that often creates confusion rather than clarity. One document that commonly falls into this category is the Reservation of Rights Letter.</p>
        <h2>What is the Reservation of Rights Letter</h2>
        <p>The Reservation of Rights Letter is a normal part of the insurance claims process. Its purpose is to provide notification from the insurance company to the policy holder that coverage may not apply. While this often comes as alarming news, the Reservation of Rights Letter should not be mistaken as an outright denial – it does not automatically mean that coverage is being or will be denied.</p>
        <p>This standard correspondence is routinely sent to comply with state laws and preserve the insurance company’s legal ability to deny some, or all, of the claim pending further investigation while the claim is ongoing and being handled by the insurance company. Failure to send the letter could be considered a waiver of their rights at a later time.</p>
        <p>Because information is vague in the early stages of a claim and often is limited to unsubstantiated allegations and a few facts, the Reservation of Rights Letter protects the insurance company’s interests to later deny coverage in whole or part based on evidence revealed during claims handling.</p>
      </div>
      <div class="col">
        <h2>Interpreting the Letter</h2>
        <p>Most of the time the Reservation of Rights Letter is a generic form letter that states your insurance company is proceeding with handling your claim but reserves the right to deny coverage later on based upon any information that reveals reason to deny.</p>
        <p>Legitimate reasons an insurance company may deny coverage include when the loss occurred in relation to your retroactive date, specific exclusions in the policy language, prior knowledge of the incident, and coverage by another policy, among others.</p>
        <p>If the insurance company believes there may be reason for denial at the time the Reservation of Rights Letter is sent, it will be stated in the letter. For example, if the claim alleges breach of warranty, the letter will state that warranties are specifically excluded by the policy and it will include the policy language to demonstrate the exclusion.</p>
        <p>Even when specific reasons for potential coverage denial are cited, it is important to note that this is not a final verdict nor does it mean complete lack of coverage. Generally the insurance company is obligated to help you if any of your claims are covered by your insurance policy – there is a duty to defend. In cases such as the scenario above, circumstances of the claim will influence what is covered and what may be subject to exclusion.</p>
        <p>Based on investigative conclusions, the insurance company may not be obligated to pay the damages for certain types or aspects of claims.</p>
      </div>
    </div>
    <div class="full">
      <h2>How to Proceed</h2>
      <p>Although the intent of the Reservation of Rights Letter is to protect the insurance company’s interests, it also alerts the policy holder to the fact that some elements of a claim may not be covered and therefore allows the insured to take steps to protect its potentially uninsured interests.</p>
      <p>However, receiving the Reservation of Rights Letter and even the insurance company’s interpretation of the policy language or law that they believe points toward coverage declination does not mean that you are automatically required to accept a denial of coverage.</p>
      <p>The best thing to do upon receiving the letter is to contact your broker and work closely with them and the insurance company claims handling department to ensure the prompt and fair handling of your claim.</p>
    </div>
  </section>
  <div class="footer-band"></div>
</article>
</body>
</html>
```